BRIGHTDESK - Remote Tech Support Site

We are looking for a new very responsive and simple website for our brand Brightdesk.com - a remote technical support company.

This company supports customers Globally in different countries throughout Eur/ North America / South America / Asia etc (please keep this in mind and integrate into the idea).

Its important to us that the design is very explanatory, the customer should easily be able to figure out that we provide computer support right away ... I like one page responsive type designs as well without a bunch of menu items

Here are some similar sites we like - but still looking for a unique design that fits out brand "brightdesk" - I have upload also some layouts i like (but the designs are not important just the layouts), youll see it includes consumer business etc which is important.

VOLM.COM - I love how clean it is - nice and white easy to see everything

PLUMWIRE247.COM - also nice the layout and responsive one page design makes it easy to use

corvalfix.com - similar to plumwire design as well - you can get the idea im looking for between the two

You will notice those examples are much different then the attachments I added - again this is more of an idea for possible layouts .. attached is also the logo - could inspire color scheme / blue white black etc

Target Market(s)

Home consumers without computer knowledge , older age 45-65, small medium business ... computer repair - slow computers

Industry/Entity Type

Computer Repair

Logo Text

Brightdesk

Coding

Coded - Design and coding required

Number of Pages Required

1 page

Font styles to use
Sans Serif
Other font styles liked:
• your choice responsive

Colors

Designer to choose colors to be used in the design.

Requirements
Must have
• Clean - responsive - professional design - the name says it all - brightdesk
• CALL TO ACTIONS FOR "Get Help Now!" / "Learn More" etc
Nice to have
• We are looking for a new very responsive and simple website for our brand Brightdesk.com - a remote technical support company.
• This company supports customers Globally in different countries throughout Eur/ North America / South America / Asia etc (please keep this in mind and integrate into the idea).
• Its important to us that the design is very explanatory, the customer should easily be able to figure out that we provide computer support right away ... I like one page responsive type designs as well without a bunch of menu items
• Here are some similar sites we like - but still looking for a unique design that fits out brand "brightdesk" - I have upload also some layouts i like (but the designs are not important just the layouts), youll see it includes consumer business etc which is important.
• VOLM.COM - I love how clean it is - nice and white easy to see everything
• PLUMWIRE247.COM - also nice the layout and responsive one page design makes it easy to use
• corvalfix.com - similar to plumwire design as well - you can get the idea im looking for between the two
Should not have
• dark, packed page - bad small font -

```html
<!DOCTYPE html>
<html lang="en">
<head>
<meta charset="utf-8">
<title>Brightdesk – Remote Tech Support</title>
<link href="https://fonts.googleapis.com/css2?family=Roboto:wght@300;400;500;700;900&display=swap" rel="stylesheet">
<style>
:root{
  --blue:#1e88f0;
  --blue-dark:#1570cc;
  --green:#5db424;
  --ink:#222;
  --text:#555;
  --muted:#888;
  --soft:#f5f5f3;
  --line:#dcdcdc;
  --black:#0b0b0b;
  --footer:#141414;
  --white:#fff;
}
*{box-sizing:border-box;margin:0;padding:0}
html,body{width:1200px;height:3429px;overflow:hidden}
body{font-family:'Roboto',Arial,sans-serif;color:var(--text);background:var(--white)}
section,header,nav,footer{position:relative;width:1200px;overflow:hidden}
.abs{position:absolute}
.btn{display:inline-flex;align-items:center;justify-content:center;font-weight:700;border-radius:3px;text-decoration:none}
.btn-blue{background:var(--blue);color:var(--white)}
.btn-dark{background:#2a2a2a;color:var(--white)}
.btn-white{background:var(--white);color:var(--blue)}

/* hero */
.hero{height:585px}
.hero-photo{position:absolute;inset:0;background:linear-gradient(90deg,#f6f5f2 0%,#ece9e4 40%,#c9c4bc 62%,#8f97a5 78%,#d8d4cc 100%)}
.hero-title{left:0;width:580px;top:58px;text-align:center;font-size:41px;font-weight:700;color:var(--blue)}
.hero-sub{left:0;width:580px;top:106px;text-align:center;font-size:36px;font-weight:300;color:var(--ink)}
.hero-list{left:86px;top:170px;display:grid;grid-template-columns:190px 230px;row-gap:12px;font-size:16px;color:#333;list-style:none}
.hero-list li{display:flex;align-items:center;gap:9px}
.hero-list b{color:var(--blue);font-weight:500}
.hero-more{left:238px;top:286px;width:105px;height:41px;font-size:17px}
.membership{left:107px;top:368px;width:371px;height:155px;background:var(--green);color:var(--white);padding:36px 0 0 34px}
.membership h3{font-size:33px;font-weight:900;letter-spacing:.5px}
.membership .price{font-size:34px;font-weight:700;margin-top:2px}
.membership .price sup{font-size:16px;vertical-align:14px}
.membership .price small{font-size:17px;font-weight:500}
.membership .start{font-size:11px;opacity:.8}
.membership .btn{position:absolute;right:32px;top:90px;width:92px;height:34px;background:#123f86;color:var(--white);font-size:12px}
.dots{right:60px;top:541px;display:flex;gap:6px}
.dots i{width:10px;height:10px;border-radius:50%;background:rgba(255,255,255,.6)}
.dots i:first-child{background:var(--white)}

/* nav */
.topnav{height:78px;background:var(--black);display:flex;align-items:stretch;color:var(--white)}
.brand{display:flex;align-items:center;gap:10px;margin-left:87px;width:267px;font-size:29px;font-weight:400;color:var(--white)}
.brand i{width:40px;height:40px;border-radius:50%;background:var(--blue)}
.menu{display:flex;list-style:none;font-size:13px;font-weight:700}
.menu li{display:flex;align-items:center;padding:0 22px}
.menu li.active{background:var(--blue)}
.menu li:nth-child(2){margin-left:10px}
.nav-right{margin-left:auto;margin-right:87px;display:flex;align-items:center;gap:30px;font-size:13px}
.nav-right .login{color:var(--blue)}

/* section headings */
.heading{position:absolute;left:0;width:1200px;text-align:center;font-weight:300;font-size:38px;color:#333;line-height:1.2}
.heading strong{font-weight:400;color:var(--blue)}
.rule{position:absolute;left:562px;width:76px;height:2px;background:#333}

/* pricing */
.pricing{height:686px;background:var(--soft)}
.plans{position:absolute;left:87px;top:192px;display:flex;gap:26px}
.plan{position:relative;width:325px;height:398px;background:var(--white);border:1px solid var(--line);text-align:center;overflow:hidden}
.plan h4{font-size:30px;font-weight:300;color:#444;margin-top:30px;height:50px}
.plan .bar{background:var(--blue);color:var(--white);height:62px;padding-top:8px}
.plan .bar .amt{font-size:28px;font-weight:700}
.plan .bar .amt small{font-size:11px}
.plan .bar .fee{font-size:11px;opacity:.7}
.plan p{font-size:15px;line-height:23px;color:#777;margin-top:38px}
.plan p b{color:#222;font-weight:500}
.plan .btn{position:absolute;left:87px;top:312px;width:151px;height:50px;font-size:15px}
.ribbon{position:absolute;right:-30px;top:14px;width:120px;height:24px;background:var(--green);transform:rotate(45deg);color:var(--white);font-size:8px;font-weight:700;text-align:center;line-height:24px}
.note{position:absolute;left:0;width:1200px;top:628px;text-align:center;font-size:12px;color:#555}
.note span{color:var(--blue)}

/* how it works */
.how{height:537px;background:var(--white)}
.steps{position:absolute;left:87px;top:162px;display:flex;gap:26px}
.step{position:relative;width:325px;height:240px;background:var(--blue);color:var(--white);text-align:center;padding:72px 28px 0}
.step .ico{position:absolute;left:124px;top:-42px;width:78px;height:78px;border-radius:50%;background:var(--white);border:4px solid var(--blue);display:flex;align-items:center;justify-content:center}
.step h4{font-size:21px;font-weight:500;line-height:24px;margin-bottom:10px}
.step p{font-size:14px;line-height:20px;color:rgba(255,255,255,.8)}
.how .btn{position:absolute;left:546px;top:434px;width:108px;height:43px;font-size:14px}

/* features */
.features{height:423px;background:#f7f6f3}
.features-photo{position:absolute;left:572px;top:0;width:628px;height:423px;background:linear-gradient(90deg,#f7f6f3 0%,#d9d2c6 30%,#9aa6b8 65%,#c9c1b3 100%)}
.feat-text{left:86px;top:64px}
.feat-text .l1{font-size:36px;font-weight:300;color:#333}
.feat-text .l2{font-size:47px;font-weight:900;color:var(--blue);line-height:1}
.feat-text .l3{font-size:36px;font-weight:300;color:#333}
.feat-text .l3 b{color:var(--green);font-weight:500}
.feat-list{list-style:none;margin-top:26px;font-size:15px;color:#333}
.feat-list li{display:flex;align-items:center;gap:12px;height:40px}

/* call */
.call{height:233px;background:linear-gradient(90deg,#1d1d1d,#4a4a4a 45%,#5b5b5b 70%,#3a3a3a);color:var(--white);text-align:center}
.call h2{position:absolute;left:0;width:1200px;top:38px;font-size:40px;font-weight:900}
.call p{position:absolute;left:0;width:1200px;top:90px;font-size:18px;line-height:24px}
.call .btn{position:absolute;left:525px;top:151px;width:150px;height:50px;font-size:16px}

/* best features */
.best{height:489px;background:var(--soft)}
.cards{position:absolute;left:87px;top:240px;display:flex;gap:28px}
.card{position:relative;width:235px;height:153px;background:var(--white);border:2px solid #8fc0f2;text-align:center;padding:56px 16px 0}
.card .ico{position:absolute;left:88px;top:-25px;width:57px;height:57px;background:var(--blue);display:flex;align-items:center;justify-content:center}
.card h5{font-size:14px;font-weight:500;color:#222;margin-bottom:8px}
.card p{font-size:12px;line-height:17px;color:#555}
.dots2{position:absolute;left:584px;top:430px;display:flex;gap:5px}
.dots2 i{width:8px;height:8px;border-radius:50%;background:#555}

/* footer */
.footer{height:364px;background:var(--footer);color:#ddd}
.footer h6{font-size:21px;font-weight:400;color:#eee;padding-bottom:10px;border-bottom:1px solid #333}
.col{position:absolute;top:58px}
.col-menu{left:85px;width:240px}
.col-menu ul{list-style:none;margin-top:12px;font-size:12px}
.col-menu li{display:flex;align-items:center;gap:14px;height:35.5px}
.col-menu li i{width:12px;height:12px;border-radius:50%;background:var(--blue)}
.col-contact{left:437px;width:325px}
.contact-row{display:flex;align-items:flex-start;gap:14px;font-size:13px;margin-top:10px;line-height:16px}
.contact-row:first-of-type{margin-top:14px}
.contact-row.phone{font-size:15px;font-weight:700}
.col-contact h6.follow{margin-top:30px}
.socials{display:flex;gap:12px;margin-top:14px}
.socials span{width:40px;height:40px;background:#2c2c2c;border-radius:3px}
.col-news{left:876px;width:240px}
.col-news p{font-size:11px;margin-top:14px}
.subscribe{display:flex;margin-top:12px;height:37px}
.subscribe span{flex:1;background:var(--black);font-size:11px;color:#777;padding:12px 10px}
.subscribe b{width:76px;background:var(--blue);color:var(--white);font-size:12px;display:flex;align-items:center;justify-content:center}
.col-news h6.trust{margin-top:26px;border:none;padding-bottom:0}
.badges{display:flex;gap:14px;margin-top:14px;align-items:center}
.badges .wide{width:92px;height:42px;background:#eee;border-radius:3px}
.badges .round{width:42px;height:42px;border-radius:50%;background:#c8c8c8}
.badges .round.gold{background:#c9a23a}
.copyright{height:34px;background:#070707;color:#666;font-size:10px;text-align:center;line-height:34px}
</style>
</head>
<body>

<header class="hero">
  <div class="hero-photo" role="img" aria-label="Photo of a man with glasses working on a laptop in a bright home office"></div>
  <h1 class="abs hero-title">Dedicated Support</h1>
  <p class="abs hero-sub">Anytime.Anywhere.</p>
  <ul class="abs hero-list">
    <li><svg width="14" height="14" viewBox="0 0 14 14"><rect x="1" y="1" width="12" height="12" fill="none" stroke="#444" stroke-width="1.5"/><path d="M3.5 7l2.5 2.5 5-6" fill="none" stroke="#1e88f0" stroke-width="2"/></svg><span><b>Instant</b> Support</span></li>
    <li><svg width="14" height="14" viewBox="0 0 14 14"><rect x="1" y="1" width="12" height="12" fill="none" stroke="#444" stroke-width="1.5"/><path d="M3.5 7l2.5 2.5 5-6" fill="none" stroke="#1e88f0" stroke-width="2"/></svg><span><b>Quick</b> Setup &amp; Intall</span></li>
    <li><svg width="14" height="14" viewBox="0 0 14 14"><rect x="1" y="1" width="12" height="12" fill="none" stroke="#444" stroke-width="1.5"/><path d="M3.5 7l2.5 2.5 5-6" fill="none" stroke="#1e88f0" stroke-width="2"/></svg><span><b>Real-Time</b> Optimization</span></li>
    <li><svg width="14" height="14" viewBox="0 0 14 14"><rect x="1" y="1" width="12" height="12" fill="none" stroke="#444" stroke-width="1.5"/><path d="M3.5 7l2.5 2.5 5-6" fill="none" stroke="#1e88f0" stroke-width="2"/></svg><span><b>Landing</b> Security Software</span></li>
    <li><svg width="14" height="14" viewBox="0 0 14 14"><rect x="1" y="1" width="12" height="12" fill="none" stroke="#444" stroke-width="1.5"/><path d="M3.5 7l2.5 2.5 5-6" fill="none" stroke="#1e88f0" stroke-width="2"/></svg><span><b>Free</b> Diagnostic</span></li>
    <li><svg width="14" height="14" viewBox="0 0 14 14"><rect x="1" y="1" width="12" height="12" fill="none" stroke="#444" stroke-width="1.5"/><path d="M3.5 7l2.5 2.5 5-6" fill="none" stroke="#1e88f0" stroke-width="2"/></svg><span><b>Unlimited</b> Cloud Backup</span></li>
  </ul>
  <a class="abs btn btn-blue hero-more">More</a>
  <div class="abs membership">
    <h3>MEMBERSHIP</h3>
    <div class="price"><sup>$</sup>19.99<small>/month</small></div>
    <div class="start">Starting at</div>
    <a class="btn">GET IT NOW</a>
  </div>
  <div class="abs dots"><i></i><i></i><i></i></div>
</header>

<nav class="topnav">
  <div class="brand"><i></i>brightdesk</div>
  <ul class="menu">
    <li class="active">HOME</li><li>ABOUT US</li><li>SERVICES</li><li>FAQs</li><li>CONTACT US</li>
  </ul>
  <div class="nav-right"><span>United States - EN</span><span class="login">Login</span></div>
</nav>

<section class="pricing">
  <h2 class="heading" style="top:48px">MEMBERSHIP<br><strong>PRICING AND</strong> PLANS</h2>
  <div class="rule" style="top:150px"></div>
  <div class="plans">
    <div class="plan">
      <h4>PREMIUM</h4>
      <div class="bar"><div class="amt">$19.99/<small>MONTHLY</small></div><div class="fee">($249-$300 setup fee)</div></div>
      <p>Regular 90-Day Optimization<br><b>Unlimited 24/7 Tier<br>3 Technician Support</b></p>
      <a class="btn btn-dark">Learn More</a>
    </div>
    <div class="plan">
      <h4>PREMIUM PLUS</h4>
      <div class="bar"><div class="amt">$29.99/<small>MONTHLY</small></div><div class="fee">($249-$300 setup fee)</div></div>
      <p>Regular 90-Day Optimization<br><b>Unlimited 24/7 Tier<br>3 Technician Support</b></p>
      <a class="btn btn-dark">Learn More</a>
    </div>
    <div class="plan">
      <div class="ribbon">POPULAR</div>
      <h4>PREMIUM</h4>
      <div class="bar"><div class="amt">$39.99/<small>MONTHLY</small></div><div class="fee">($249-$300 setup fee)</div></div>
      <p>Regular 90-Day Optimization<br><b>Unlimited 24/7 Tier<br>3 Technician Support<br>Online Identity Theft Protection</b></p>
      <a class="btn btn-dark">Learn More</a>
    </div>
  </div>
  <p class="note"><span>✔ FREE</span> Optimization and Diagnostic when you call in. Limited time offer.</p>
</section>

<section class="how">
  <h2 class="heading" style="top:52px">HOW IT <strong>WORKS</strong></h2>
  <div class="rule" style="top:110px"></div>
  <div class="steps">
    <div class="step">
      <div class="ico"><svg width="34" height="30" viewBox="0 0 34 30"><rect x="3" y="16" width="6" height="12" fill="#1e88f0"/><rect x="11" y="10" width="6" height="18" fill="#1e88f0"/><rect x="19" y="4" width="6" height="24" fill="#1e88f0"/><rect x="27" y="12" width="5" height="16" fill="#1e88f0"/></svg></div>
      <h4>FREE DIAGNOSTIC</h4>
      <p>Get a diagnostic, FOR FREE! Get a free consultation with our staff.</p>
    </div>
    <div class="step">
      <div class="ico"><svg width="32" height="32" viewBox="0 0 32 32"><path d="M5 27L22 10M10 5l17 17" stroke="#1e88f0" stroke-width="4" stroke-linecap="round"/><circle cx="24" cy="8" r="5" fill="none" stroke="#1e88f0" stroke-width="3"/></svg></div>
      <h4>GET FIXED</h4>
      <p>Get fixed, IMMEDIATELY! Our staff will solve your computer issues right before your eyes.</p>
    </div>
    <div class="step">
      <div class="ico"><svg width="32" height="32" viewBox="0 0 32 32"><path d="M4 18v9h24v-9" fill="none" stroke="#1e88f0" stroke-width="3"/><path d="M11 20V8M21 20V8M7 11l4-5 4 5M17 11l4-5 4 5" fill="none" stroke="#1e88f0" stroke-width="3"/></svg></div>
      <h4>BACKUP<br>YOUR INFORMATION!</h4>
      <p>Saving your files is now EASY! You will be able to retain your personal files without any loss of data.</p>
    </div>
  </div>
  <a class="btn btn-dark">Read More</a>
</section>

<section class="features">
  <div class="features-photo" role="img" aria-label="Photo of a smiling senior man using a laptop at home"></div>
  <div class="abs feat-text">
    <div class="l1">REAL-TIME</div>
    <div class="l2">SUPPORT FEATURES</div>
    <div class="l3">AND <b>BENEFITS</b></div>
    <ul class="feat-list">
      <li><svg width="14" height="14" viewBox="0 0 14 14"><rect x="1" y="1" width="12" height="12" fill="none" stroke="#1e88f0" stroke-width="1.5"/><path d="M3.5 7l2.5 2.5 5-6" fill="none" stroke="#1e88f0" stroke-width="2"/></svg>24/7 Real-Time Technician Support</li>
      <li><svg width="14" height="14" viewBox="0 0 14 14"><rect x="1" y="1" width="12" height="12" fill="none" stroke="#1e88f0" stroke-width="1.5"/><path d="M3.5 7l2.5 2.5 5-6" fill="none" stroke="#1e88f0" stroke-width="2"/></svg>The best Security Software in the market</li>
      <li><svg width="14" height="14" viewBox="0 0 14 14"><rect x="1" y="1" width="12" height="12" fill="none" stroke="#1e88f0" stroke-width="1.5"/><path d="M3.5 7l2.5 2.5 5-6" fill="none" stroke="#1e88f0" stroke-width="2"/></svg>Regular tune-ups and optimization</li>
      <li><svg width="14" height="14" viewBox="0 0 14 14"><rect x="1" y="1" width="12" height="12" fill="none" stroke="#1e88f0" stroke-width="1.5"/><path d="M3.5 7l2.5 2.5 5-6" fill="none" stroke="#1e88f0" stroke-width="2"/></svg>Setup and installation included</li>
    </ul>
  </div>
</section>

<section class="call" role="img" aria-label="Dark photo of a circuit board and hands on a keyboard behind the call to action">
  <h2>CALL US TODAY</h2>
  <p>And get started with our dedicated<br>technicians.</p>
  <a class="btn btn-white">Get Help Now!</a>
</section>

<section class="best">
  <h2 class="heading" style="top:62px">ALL THE BEST FEATURES,<br><strong>AT THE BEST PRICE!</strong></h2>
  <div class="rule" style="top:162px"></div>
  <div class="cards">
    <div class="card">
      <div class="ico"><svg width="30" height="26" viewBox="0 0 30 26"><rect x="2" y="2" width="22" height="16" fill="none" stroke="#fff" stroke-width="2"/><circle cx="20" cy="16" r="5" fill="none" stroke="#fff" stroke-width="2"/><path d="M24 20l4 4" stroke="#fff" stroke-width="2"/></svg></div>
      <h5>AD BLOCKER</h5><p>Avoid unwanted Pop-ups with the newest Ad Blocking technology.</p>
    </div>
    <div class="card">
      <div class="ico"><svg width="30" height="26" viewBox="0 0 30 26"><rect x="2" y="2" width="26" height="17" fill="none" stroke="#fff" stroke-width="2"/><path d="M10 24h10M15 19v5M6 15l5-5 4 3 7-6" fill="none" stroke="#fff" stroke-width="2"/></svg></div>
      <h5>REGULAR TUNE-UPS</h5><p>Get a Regular Tune-Up and Optimization every 90 days.</p>
    </div>
    <div class="card">
      <div class="ico"><svg width="28" height="28" viewBox="0 0 28 28"><rect x="3" y="3" width="22" height="6" fill="none" stroke="#fff" stroke-width="2"/><rect x="3" y="11" width="22" height="6" fill="none" stroke="#fff" stroke-width="2"/><rect x="3" y="19" width="22" height="6" fill="none" stroke="#fff" stroke-width="2"/></svg></div>
      <h5>SYSTEM REPORTS</h5><p>Stay up to date with Real-Time System Reporting.</p>
    </div>
    <div class="card">
      <div class="ico"><svg width="32" height="26" viewBox="0 0 32 26"><rect x="2" y="2" width="20" height="14" fill="none" stroke="#fff" stroke-width="2"/><rect x="20" y="8" width="10" height="16" fill="#1e88f0" stroke="#fff" stroke-width="2"/><path d="M6 22h12" stroke="#fff" stroke-width="2"/></svg></div>
      <h5>MULTIPLE DEVICES</h5><p>Get support for up to 4 multiple devices. Ask about our Family Plans.</p>
    </div>
  </div>
  <div class="dots2"><i></i><i></i><i></i></div>
</section>

<footer class="footer">
  <div class="col col-menu">
    <h6>Manu</h6>
    <ul><li><i></i>HOME</li><li><i></i>ABOUT US</li><li><i></i>SERVICES</li><li><i></i>FAQs</li><li><i></i>CONTACT US</li></ul>
  </div>
  <div class="col col-contact">
    <h6>Contact Information</h6>
    <div class="contact-row phone"><svg width="14" height="14" viewBox="0 0 14 14"><rect width="14" height="14" rx="2" fill="#1e88f0"/><path d="M4 3l2 2-1 1.5c.6 1.2 1.3 1.9 2.5 2.5L9 8l2 2-1.5 1.5C6 11 3 8 2.5 4.5z" fill="#fff"/></svg>(888) 555-0142</div>
    <div class="contact-row"><svg width="14" height="12" viewBox="0 0 14 12"><rect width="14" height="12" rx="1" fill="#1e88f0"/><path d="M1 2l6 5 6-5" fill="none" stroke="#fff" stroke-width="1.4"/></svg>info@brightdesk.com</div>
    <div class="contact-row"><svg width="14" height="16" viewBox="0 0 14 16"><path d="M7 0a6 6 0 016 6c0 4-6 10-6 10S1 10 1 6a6 6 0 016-6z" fill="#1e88f0"/><circle cx="7" cy="6" r="2" fill="#141414"/></svg><span>Northvane Ltd, 4410 Harbour St. 3rd Floor,<br>Halifax, NS B3J 0A1 Canada</span></div>
    <h6 class="follow">Follow Us</h6>
    <div class="socials"><span aria-label="Social profile link"></span><span aria-label="Social profile link"></span></div>
  </div>
  <div class="col col-news">
    <h6>Newsletter Signup</h6>
    <p>Sign up for our regular informational newsletters</p>
    <div class="subscribe"><span>Enter your email id</span><b>Signup</b></div>
    <h6 class="trust">Trusted By</h6>
    <div class="badges" aria-label="Review and security badges"><span class="wide"></span><span class="round"></span><span class="round gold"></span></div>
  </div>
</footer>
<div class="copyright">Brightdesk © 2017. All rights reserved. Terms and Conditions · Refund Policy · Privacy Policy</div>

</body>
</html>
```